Banner Ad Design Project

I need a banner design. The website is under construction at www.brightmarrow.example

Name: Bright Marrow
Tagline: Steady Sparks for crowded calendars

This is a leadership development and executive coaching site. The past site is live at www.quillstepnow.example. (so you can get a sense of the content)

The audience are (BUSY) executives, senior managers, leaders and top professionals, so the feel needs to be highly professional but also modern and fresh. I want to communicate energy but also solid and trust worthy and not too new agey. The audience are also people with strong social values who want to change things - so not too corporate (Ie suits!)

I would like the design to be floating on a white background, very clean and simple. I am attracted to reds or sunset (burn orange crimson colors.) But totally open to any color ideas.
I am giving an open brief for your ideas.
Here are the dimensions 960px wide, roughly 190px height.

Reason: The weekend might give more time to designers to get involved. Thanks Vina

Hi designers

You may not have seen the additions I gave to this brief.

The banner should not have leader out front photo's. Maybe less corporate than I initially thought. 
Not too corporate (no suits!) Please no chess pieces, jigsaw pieces, cartoon images, cliche leadership images. 
Am am trying for inspiration /inspiring whilst still being professional. Very simple and clean.
Please can the design be floating in a white background so that the web page is borderless - A bit like it is in http://palmoriskel.example/
Thank you

Target Market(s)

Senior managers, executives but people who also want to change the world!

Industry/Entity Type

Construction

Requirements
Should not have
• Should not have leader out front photo's.
Maybe less corporate than I initially thought.
Am am trying for inspiration /inspiring whilst still being professional.
Please no chess pieces, jigsaw pieces, cartoon images, cliche leadership images. Not too corporate (Ie suits!)

Thanks

```html
<!DOCTYPE html>
<html lang="en">
<head>
<meta charset="utf-8">
<title>Bright Marrow — Banner</title>
<link rel="stylesheet" href="https://fonts.googleapis.com/css2?family=Open+Sans:wght@600&display=swap">
<style>
  :root {
    --paper: #ffffff;
    --ink: #2a2624;
    --rule: #c9c4c0;
    --photo-warm: #d9c6ad;
    --photo-deep: #7a5a3e;
  }
  html, body {
    margin: 0;
    padding: 0;
    overflow: hidden;
    background: var(--paper);
  }
  .banner {
    position: relative;
    width: 1200px;
    height: 238px;
    background: var(--paper);
    overflow: hidden;
  }
  .brand-name {
    position: absolute;
    left: 48px;
    top: 34px;
    margin: 0;
    font-family: "Open Sans", Arial, sans-serif;
    font-weight: 600;
    font-size: 80px;
    line-height: 1.1;
    letter-spacing: -1px;
    color: var(--ink);
    white-space: nowrap;
  }
  .brand-rule {
    position: absolute;
    left: 50px;
    top: 151px;
    width: 714px;
    height: 1px;
    background: var(--rule);
  }
  .tagline {
    position: absolute;
    left: 86px;
    top: 168px;
    margin: 0;
    font-family: "Open Sans", Arial, sans-serif;
    font-weight: 600;
    font-size: 17px;
    letter-spacing: 4.6px;
    text-transform: uppercase;
    color: var(--ink);
    white-space: nowrap;
  }
  .hero-photo {
    position: absolute;
    right: 0;
    top: 0;
    width: 340px;
    height: 238px;
    background:
      radial-gradient(ellipse 90px 95px at 52% 42%, var(--photo-warm) 0%, rgba(217,198,173,0.5) 60%, rgba(255,255,255,0) 100%),
      radial-gradient(ellipse 150px 70px at 80% 85%, var(--photo-deep) 0%, rgba(122,90,62,0.35) 55%, rgba(255,255,255,0) 100%),
      linear-gradient(90deg, var(--paper) 0%, #f4eee8 60%, #efe6dc 100%);
  }
</style>
</head>
<body>
  <header class="banner">
    <h1 class="brand-name">Bright Marrow</h1>
    <div class="brand-rule"></div>
    <p class="tagline">Steady Sparks for crowded calendars</p>
    <div class="hero-photo" role="img" aria-label="Photograph of an open hand holding a glass globe against a soft warm background"></div>
  </header>
</body>
</html>
```